New Business Cards for Organic Meat Farm

We need a business card designed for Thornbury Farm, a meat farm in western MA. Our logo uses a hand-drawn woodcut (attached). Our color palette has been simply black and white (shown in notepad and picture of our food truck). While we are based out of western MA, we have ambitions to grow nationally, so our hope is for a classy and memorable card which will be printed on a premium quality stock from a printer like printkestrel.com.
Target Market(s)
consumers of quality meats, restauranteurs, partnering farms
Industry/Entity Type
Farming and prepared meat products
Contact Information for Business Card
Wendell Pruitt, President/Owner, wendell@thornburyfarm.com, mobile: 413-555-0172, phone: 413-555-0148, thornburyfarm.com, facebook: @thornburyfarm, instagram: @thornburyfarmma
Colors
Designer to choose colors to be used in the design.
Look and feel

```html
<!DOCTYPE html>
<html lang="en">
<head>
<meta charset="UTF-8">
<title>Thornbury Farm — Business Card</title>
<link href="https://fonts.googleapis.com/css2?family=Lato:wght@400;700;900&display=swap" rel="stylesheet">
<style>
  :root {
    --backdrop: #e6e6e6;
    --card: #ffffff;
    --ink: #111111;
    --ink-soft: #555555;
    --rule: #c8c8c8;
    --art-dark: #2a2a2a;
    --art-light: #9a9a9a;
  }
  * { box-sizing: border-box; margin: 0; padding: 0; }
  html, body {
    width: 1200px; height: 900px; overflow: hidden;
    background: var(--backdrop);
    font-family: "Lato", sans-serif;
    color: var(--ink);
  }
  .sheet {
    width: 1200px; height: 900px;
    display: flex; flex-direction: column;
    align-items: center; justify-content: center; gap: 40px;
  }
  .card {
    width: 700px; height: 400px;
    background: var(--card);
    border-radius: 36px;
    box-shadow: 0 6px 18px rgba(0,0,0,0.12);
    position: relative;
  }
  .woodcut {
    background: radial-gradient(ellipse at 50% 55%, var(--art-dark) 0%, #555 45%, var(--art-light) 75%, rgba(255,255,255,0) 100%);
    border-radius: 8px;
  }
  .card-front { display: flex; align-items: center; justify-content: center; }
  .card-front .woodcut { width: 300px; height: 170px; }

  .card-back { display: flex; }
  .brand {
    width: 52%;
    display: flex; flex-direction: column; align-items: center; justify-content: center;
    padding-top: 10px;
  }
  .brand .woodcut { width: 300px; height: 170px; }
  .brand-name {
    margin-top: 18px;
    font-weight: 900; font-size: 46px; line-height: 1;
    text-align: center; letter-spacing: 0.5px;
  }
  .brand-name span { display: block; font-size: 28px; letter-spacing: 10px; margin-top: 8px; }
  .divider {
    width: 1px; margin: 40px 0;
    background: linear-gradient(to bottom, rgba(0,0,0,0), var(--rule) 30%, var(--rule) 70%, rgba(0,0,0,0));
  }
  .contact {
    flex: 1; padding: 70px 0 0 34px;
  }
  .contact-name { font-weight: 700; font-size: 22px; letter-spacing: 0.5px; }
  .contact-title { font-size: 17px; color: var(--ink-soft); margin-top: 2px; }
  .contact-list { list-style: none; margin-top: 26px; }
  .contact-list li {
    display: flex; align-items: center; gap: 10px;
    font-size: 17px; color: #333; height: 27px;
  }
  .contact-list svg { width: 16px; height: 16px; flex: none; }
</style>
</head>
<body>
<main class="sheet">
  <section class="card card-front">
    <div class="woodcut" role="img" aria-label="Hand-drawn woodcut illustration of the farmhouse with porch, surrounded by trees"></div>
  </section>

  <section class="card card-back">
    <div class="brand">
      <div class="woodcut" role="img" aria-label="Hand-drawn woodcut illustration of the farmhouse with porch, surrounded by trees"></div>
      <div class="brand-name">Thornbury<span>FARM</span></div>
    </div>
    <div class="divider"></div>
    <div class="contact">
      <div class="contact-name">WENDELL PRUITT</div>
      <div class="contact-title">President/OwnerDirector</div>
      <ul class="contact-list">
        <li>
          <svg viewBox="0 0 16 16" aria-hidden="true"><rect x="4" y="1" width="8" height="14" rx="1.5" fill="none" stroke="#111" stroke-width="1.3"/><line x1="7" y1="12.5" x2="9" y2="12.5" stroke="#111" stroke-width="1.2"/></svg>
          413-555-0172
        </li>
        <li>
          <svg viewBox="0 0 16 16" aria-hidden="true"><path d="M3 2l3 0 1 3.5-2 1.2c.8 1.8 2.2 3.2 4 4l1.2-2 3.5 1 0 3c-6.5.3-11-4.2-10.7-10.7z" fill="#111"/></svg>
          413-555-0148
        </li>
        <li>
          <svg viewBox="0 0 16 16" aria-hidden="true"><rect x="1" y="3" width="14" height="10" fill="#111"/><path d="M1 3l7 6 7-6" fill="none" stroke="#fff" stroke-width="1.2"/></svg>
          wendell@thornburyfarm.com
        </li>
        <li>
          <svg viewBox="0 0 16 16" aria-hidden="true"><circle cx="8" cy="8" r="6.5" fill="none" stroke="#111" stroke-width="1.2"/><ellipse cx="8" cy="8" rx="3" ry="6.5" fill="none" stroke="#111" stroke-width="1"/><line x1="1.5" y1="8" x2="14.5" y2="8" stroke="#111" stroke-width="1"/></svg>
          thornburyfarm.com
        </li>
        <li>
          <svg viewBox="0 0 16 16" aria-hidden="true"><circle cx="8" cy="8" r="7" fill="#111"/></svg>
          @thornburyfarm
        </li>
        <li>
          <svg viewBox="0 0 16 16" aria-hidden="true"><circle cx="8" cy="8" r="7" fill="#111"/></svg>
          @thornburyfarmma
        </li>
      </ul>
    </div>
  </section>
</main>
</body>
</html>
```